Brochure/flyer for our trip to Paris

Our company is taking us all on a summer trip to Paris. We have some key information that we need to tell everybody about the trip. We think a nicely designed brochure or flyer, which uses our brand colours and guidelines, would be something nice to keep during the trip and as a memento afterwards.

We are looking for a brochure or a flyer which contains all the info in the attached document.

This needs to happen really fast as we actually go to Paris on the 13th August. We also need time to print it!

We can provide a library of icons. All images in the document can be changed. you don't have to use the images in the document.

Target Market(s)

People in our company. They are fun and as this is for a party the flyer needs to feel uplifting.

Industry/Entity Type

Health

Font styles to use
Other font styles liked:
• Nexa - please see attached font.

Requirements
Must have
• Designers must stick to our brand guideline, font and the colours we use.
• Please also see attached content for the flyer.
• This website shows our style - https://www.korilune.com/fr
Should not have
• Please don't make it too tacky or too much about French things. It can be a bit playful but not too much.

```html
<!DOCTYPE html>
<html lang="en">
<head>
<meta charset="utf-8">
<title>Korilune – Paris 2016</title>
<link rel="stylesheet" href="https://fonts.googleapis.com/css2?family=Urbanist:wght@300;600&display=swap">
<style>
  :root {
    --band-navy: #3a4e98;
    --band-teal: #69c2c5;
    --band-orange: #eb5a29;
    --band-blue: #4287c7;
    --text-white: #ffffff;
  }
  html, body {
    margin: 0;
    padding: 0;
    overflow: hidden;
    background: #ffffff;
  }
  .flyer {
    position: relative;
    width: 770px;
    height: 1200px;
    overflow: hidden;
    font-family: "Urbanist", sans-serif;
    color: var(--text-white);
  }
  .band {
    position: absolute;
    left: 0;
    width: 100%;
    height: 300px;
  }
  .band--navy   { top: 0;     background: var(--band-navy); }
  .band--teal   { top: 300px; background: var(--band-teal); }
  .band--orange { top: 600px; background: var(--band-orange); }
  .band--blue   { top: 900px; background: var(--band-blue); }

  .brand-name {
    position: absolute;
    left: 0;
    width: 100%;
    top: 516px;
    margin: 0;
    text-align: center;
    font-weight: 600;
    font-size: 136px;
    line-height: 1;
    letter-spacing: -1px;
  }
  .trip-title {
    position: absolute;
    left: 0;
    width: 100%;
    top: 673px;
    margin: 0;
    text-align: center;
    font-weight: 300;
    font-size: 40px;
    line-height: 1;
    letter-spacing: 0.5px;
  }
</style>
</head>
<body>
  <main class="flyer">
    <div class="band band--navy"></div>
    <div class="band band--teal"></div>
    <div class="band band--orange"></div>
    <div class="band band--blue"></div>

    <h1 class="brand-name">Korilune</h1>
    <p class="trip-title">Paris 2016</p>
  </main>
</body>
</html>
```